Business Card for Makeup Artist

I need a business card designed for my makeup and hair artistry business which is primarily events and weddings focused. The card needs to be sleek, simple, stylish and appealing to women. I would prefer a white background but open to suggestions also. I also love the marble background look. I have attached some example pics. It needs to be a double sided card with logo and/or design on one side and contact details in the centre of the card on the other side. NO LOGO ON BACK. Examples attached.

Target Market(s)

Females age 14-55

Industry/Entity Type

Business

Contact Information for Business Card

Nora Vint
Principal Makeup Artist
P: 0413 925 214
E: nora@lumirabeauty.com.au
W: www.lumirabeauty.com.au

Requirements
Should not have
• No yellow, green, red or blue in the design.

```html
<!DOCTYPE html>
<html lang="en">
<head>
<meta charset="utf-8">
<title>Lumira Makeup Artistry – Business Card</title>
<link href="https://fonts.googleapis.com/css2?family=Lato:ital,wght@0,300;0,400;1,400&display=swap" rel="stylesheet">
<style>
  :root {
    --stage: #e9e7e8;
    --card-white: #ffffff;
    --ink: #1c1a1b;
    --logo-grey: #555354;
    --frame-black: #1a1819;
    --plum: #6e2a5e;
    --magenta: #a83a7e;
    --mauve: #b57aa8;
    --blush: #ecb6c8;
    --lilac: #c9a9d6;
    --orchid: #d58fbf;
  }
  * { box-sizing: border-box; margin: 0; padding: 0; }
  html, body {
    width: 1200px;
    height: 873px;
    overflow: hidden;
    background: var(--stage);
    font-family: "Lato", Arial, sans-serif;
  }
  .card-set {
    position: absolute;
    inset: 0;
    display: flex;
    align-items: center;
    justify-content: center;
    gap: 60px;
  }
  .card {
    position: relative;
    width: 525px;
    height: 300px;
    background: var(--card-white);
    overflow: hidden;
    box-shadow: 0 10px 28px rgba(0,0,0,0.14);
  }

  /* Front side */
  .card-front__backdrop {
    position: absolute;
    inset: 0;
    background:
      radial-gradient(circle at 12% 28%, var(--plum) 0, transparent 24%),
      radial-gradient(circle at 30% 8%, var(--orchid) 0, transparent 22%),
      radial-gradient(circle at 78% 80%, var(--plum) 0, transparent 22%),
      radial-gradient(circle at 88% 18%, var(--blush) 0, transparent 24%),
      radial-gradient(circle at 15% 88%, var(--orchid) 0, transparent 24%),
      radial-gradient(circle at 55% 50%, var(--lilac) 0, transparent 40%),
      linear-gradient(120deg, var(--magenta), var(--blush) 45%, var(--mauve) 75%, var(--magenta));
    filter: blur(6px);
    transform: scale(1.08);
  }
  .logo-frame {
    position: absolute;
    left: 50%;
    top: 50%;
    width: 310px;
    height: 150px;
    transform: translate(-50%, -50%);
    background: var(--card-white);
    border: 12px solid var(--frame-black);
    display: flex;
    flex-direction: column;
    align-items: center;
    justify-content: center;
  }
  .brand-name {
    font-size: 50px;
    font-weight: 400;
    color: var(--logo-grey);
    letter-spacing: 0.04em;
    line-height: 1;
  }
  .brand-tagline {
    font-size: 17px;
    font-weight: 300;
    color: var(--logo-grey);
    letter-spacing: 0.06em;
    text-transform: uppercase;
    margin-top: 6px;
  }

  /* Back side */
  .corner-wave {
    position: absolute;
    left: 0;
    top: 0;
    width: 70px;
    height: 300px;
  }
  .wave-top { stop-color: var(--lilac); }
  .wave-mid { stop-color: var(--orchid); }
  .wave-end { stop-color: var(--magenta); }
  .contact {
    position: absolute;
    inset: 0;
    display: flex;
    flex-direction: column;
    align-items: center;
    justify-content: center;
    text-align: center;
    color: var(--ink);
  }
  .contact__name {
    font-size: 20px;
    font-weight: 400;
    letter-spacing: 0.02em;
    text-transform: uppercase;
  }
  .contact__role {
    font-size: 13px;
    font-style: italic;
    margin-top: 3px;
  }
  .contact__list {
    list-style: none;
    margin-top: 22px;
    font-size: 13px;
    line-height: 1.55;
    letter-spacing: 0.02em;
  }
</style>
</head>
<body>
<main class="card-set">
  <section class="card card-front" aria-label="Card front">
    <div class="card-front__backdrop" role="img" aria-label="Soft blurred watercolour wash in plum, orchid, lilac and blush pink"></div>
    <div class="logo-frame">
      <span class="brand-name">Lumira</span>
      <span class="brand-tagline">Makeup Artistry</span>
    </div>
  </section>

  <section class="card card-back" aria-label="Card back">
    <svg class="corner-wave" viewBox="0 0 70 300" aria-hidden="true">
      <defs>
        <linearGradient id="waveTone" x1="0" y1="0" x2="0" y2="1">
          <stop offset="0" class="wave-top"/>
          <stop offset="0.55" class="wave-mid"/>
          <stop offset="1" class="wave-end"/>
        </linearGradient>
      </defs>
      <path d="M0 0 H52 C40 30 66 55 58 90 C50 125 20 120 28 160 C34 190 14 200 0 210 Z" fill="url(#waveTone)"/>
    </svg>
    <div class="contact">
      <p class="contact__name">Nora Vint</p>
      <p class="contact__role">Principal Makeup Artist</p>
      <ul class="contact__list">
        <li>0413 925 214</li>
        <li>nora@lumirabeauty.com.au</li>
        <li>www.lumirabeauty.com.au</li>
      </ul>
    </div>
  </section>
</main>
</body>
</html>
```